[WEB DESIGN - Start-up] Online LOANS against Luxury Assets - Needs a Web Design

Hello,
We need a web design for a new company. We make online LOANS against Luxury assets.
The name is private, that's why you could remplace it by the term "LOGO" or "ENTERPRISE".

In attachments, you'll find few models that we would like. Nonetheless, we don't want a copy of these screenshots. They are only prototypes that we made. Here we expect you to lead a professional web Design with your intuition and your ideas.

The final design should communicate start-up spirit, professionalism and fluidity.

Best Regards.

Industry/Entity Type

Finance

Number of Pages Required

2 page

Font styles to use
Sans Serif

Colors
f78f20
ffffff
b2b2b2
e9e9e9

Requirements
Must have
• The designer will draw on the 2015 web trends.
• The subject site is serious (loans against luxury assets), but the site should be modern and pleasant.
• PLEASE REFER YOU TO MY MODEL ( ATTACHMENTS)
Nice to have
• Surprise-me ! Welcome to a lot of imagination.

```html
<!DOCTYPE html>
<html lang="fr">
<head>
<meta charset="utf-8">
<title>Enterprise — Prêts sur biens de luxe</title>
<link href="https://fonts.googleapis.com/css2?family=Open+Sans:wght@400;600;700&family=Oswald:wght@400;500&display=swap" rel="stylesheet">
<style>
:root{
  --orange:#f78f20;
  --orange-dark:#e07a10;
  --white:#ffffff;
  --grey:#b2b2b2;
  --light:#e9e9e9;
  --ink:#333333;
  --dark:#2b2b2b;
  --darker:#1f1f1f;
  --text:#666666;
}
*{box-sizing:border-box;margin:0;padding:0}
html,body{width:711px;height:1200px;overflow:hidden}
body{font-family:"Open Sans",Arial,sans-serif;color:var(--ink);background:var(--white);font-size:7px;line-height:1.45}
.page{width:711px;height:1200px;position:relative}

/* header */
.topbar{height:28px;background:var(--orange);display:flex;align-items:center;padding:0 22px;color:var(--white)}
.brand{font-weight:700;font-size:13px;letter-spacing:.5px}
.nav{margin-left:auto;display:flex;gap:14px;font-size:6.5px;font-weight:600}
.social{display:flex;gap:4px;margin-left:18px}
.social span{width:13px;height:13px;border-radius:50%;background:var(--white);opacity:.9}

/* hero */
.hero{height:277px;position:relative;background:linear-gradient(100deg,#d7d5d2 0%,#efeeec 45%,#c9c6c2 100%);text-align:center}
.hero-photo{position:absolute;inset:0}
.hero h1{position:relative;padding-top:62px;font-family:"Oswald",Arial,sans-serif;font-weight:500;font-size:33px;line-height:1.12;color:var(--white);text-shadow:0 1px 3px rgba(0,0,0,.35)}
.btn-read{position:relative;display:inline-block;margin-top:22px;padding:9px 26px;background:var(--white);border:2px solid var(--orange);color:var(--orange);font-size:15px}

/* search */
.search{height:25px;background:var(--darker);display:flex;align-items:center;gap:6px;padding:0 22px;color:var(--white)}
.search b{font-size:6.5px;margin-right:4px}
.select{height:14px;background:var(--white);width:118px;font-size:6px;color:var(--text);padding:2px 4px;position:relative}
.select:after{content:"";position:absolute;right:4px;top:5px;border:3px solid transparent;border-top-color:var(--text)}
.btn-search{margin-left:auto;height:15px;width:88px;background:var(--orange);font-size:6.5px;text-align:center;line-height:15px}

/* features */
.features{height:145px;background:var(--light);display:flex;justify-content:space-around;padding:18px 40px 0}
.feature{width:118px;text-align:center}
.feature .circle{width:46px;height:46px;border-radius:50%;background:var(--white);border:2px solid var(--orange);margin:0 auto 7px;display:flex;align-items:center;justify-content:center}
.feature h3{font-size:9px;font-weight:600;color:var(--orange);margin-bottom:5px}
.feature p{font-size:5.5px;color:var(--text)}

/* assets */
.assets{height:155px;padding:14px 22px 0}
.section-head{display:flex;justify-content:space-between;font-size:8px;font-weight:700}
.section-head small{font-size:6.5px}
.carousel{display:flex;align-items:center;gap:8px;margin-top:16px}
.arrow{width:15px;height:15px;border-radius:50%;background:var(--orange);flex:none;display:flex;align-items:center;justify-content:center}
.asset{flex:1;text-align:center}
.asset-photo{height:62px}
.asset span{display:block;margin-top:5px;font-size:6px;font-weight:700;color:var(--orange)}

/* help */
.help{height:160px;background:var(--orange);color:var(--white);text-align:center}
.help h2{font-size:8px;font-weight:700;padding:14px 0 12px}
.help-cols{display:flex;padding:0 40px}
.help-col{flex:1;border-right:1px solid rgba(255,255,255,.45);padding-top:4px}
.help-col:last-child{border:none}
.help-col p{font-size:6px;margin-top:8px}
.help-col strong{display:block;font-size:9px;margin-top:2px}

/* testimonials */
.testimonials{height:100px;text-align:center;padding:10px 60px 0}
.testimonials h2{font-size:8px;font-weight:700;margin-bottom:10px}
.testimonials p{font-size:5.5px;color:var(--text)}
.testimonials .quote-sign{color:var(--orange);font-size:6px;margin-top:6px}
.dots{display:flex;justify-content:center;gap:4px;margin-top:6px}
.dots i{width:5px;height:5px;border-radius:50%;background:var(--grey)}
.dots i:first-child{background:var(--orange)}

/* counters */
.counters{height:150px;display:flex;border-top:1px solid var(--light);padding:20px 30px 0;gap:40px}
.counter{flex:1;text-align:center}
.digits{display:inline-flex;gap:2px}
.digits span{width:22px;height:32px;background:var(--darker);color:var(--white);font-family:"Oswald",Arial,sans-serif;font-size:20px;line-height:32px;position:relative}
.digits span:after{content:"";position:absolute;left:0;right:0;top:16px;height:1px;background:#555}
.counter p{color:var(--orange);font-size:7px;font-weight:600;margin-top:12px;text-align:left;padding:0 10px}

/* footer */
.footer{height:140px;background:var(--dark);color:var(--grey);padding:12px 22px 0}
.footer-intro{display:flex;gap:10px;align-items:center;font-size:5px;border-bottom:1px solid #444;padding-bottom:8px}
.footer-intro .badge{width:22px;height:22px;border-radius:50%;background:#444;flex:none}
.footer-cols{display:flex;gap:20px;padding-top:8px}
.footer-about{flex:2.2}
.footer-about h4,.footer-contact h4{color:var(--orange);font-size:10px;font-weight:600;margin-bottom:4px}
.footer-about p,.footer-contact p{font-size:5.5px}
.footer-links{flex:.8;font-size:5.5px;list-style:none}
.footer-contact{flex:1.6}
.bottombar{height:20px;background:var(--darker);color:var(--grey);display:flex;align-items:center;padding:0 22px;font-size:5.5px}
.bottombar .social{margin-left:6px}
.bottombar .social span{background:var(--grey);width:11px;height:11px}
.bottombar .follow{margin-left:auto}
</style>
</head>
<body>
<div class="page">

  <header class="topbar">
    <div class="brand">ENTERPRISE</div>
    <nav class="nav"><span>Concept</span><span>Nos biens</span><span>Estimation</span><span>FAQ</span><span>Contact</span></nav>
    <div class="social"><span></span><span></span><span></span></div>
  </header>

  <section class="hero">
    <div class="hero-photo" role="img" aria-label="Photo : mains tenant une tablette et un smartphone près d'une tasse de café sur un bureau clair"></div>
    <h1>ON SE LASSE DE TOUT,<br>SAUF DE L'ARGENT</h1>
    <a class="btn-read">Read More</a>
  </section>

  <form class="search">
    <b>NATURE DE L'OBJET</b>
    <div class="select">Sélectionnez</div>
    <div class="select">Sélectionnez</div>
    <div class="select">Sélectionnez</div>
    <div class="btn-search">Rechercher</div>
  </form>

  <section class="features">
    <div class="feature">
      <div class="circle"><svg width="22" height="22" viewBox="0 0 24 24" fill="none" stroke="#f78f20" stroke-width="2"><circle cx="10" cy="10" r="6"/><path d="M15 15l6 6"/></svg></div>
      <h3>ESTIMATION</h3>
      <p>Nos experts évaluent votre bien en quelques heures, gratuitement et sans aucun engagement de votre part.</p>
    </div>
    <div class="feature">
      <div class="circle"><svg width="22" height="22" viewBox="0 0 24 24" fill="none" stroke="#f78f20" stroke-width="2"><rect x="3" y="6" width="18" height="12" rx="1"/><circle cx="12" cy="12" r="3"/></svg></div>
      <h3>PAIEMENT</h3>
      <p>Après acceptation, vous recevez jusqu'à 70% de la valeur estimée directement sur votre compte.</p>
    </div>
    <div class="feature">
      <div class="circle"><svg width="22" height="22" viewBox="0 0 24 24" fill="none" stroke="#f78f20" stroke-width="2"><rect x="5" y="11" width="14" height="10" rx="1"/><path d="M8 11V7a4 4 0 018 0v4"/></svg></div>
      <h3>SECURISATION</h3>
      <p>Votre bien est stocké dans nos coffres sécurisés et assuré pendant toute la durée du prêt.</p>
    </div>
    <div class="feature">
      <div class="circle"><svg width="22" height="22" viewBox="0 0 24 24" fill="none" stroke="#f78f20" stroke-width="2"><path d="M4 12a8 8 0 0114-5M20 12a8 8 0 01-14 5"/><path d="M18 3v4h-4M6 21v-4h4"/></svg></div>
      <h3>RACHAT</h3>
      <p>À tout moment, remboursez votre prêt et récupérez votre bien dans son état d'origine.</p>
    </div>
  </section>

  <section class="assets">
    <div class="section-head"><span>LES BIENS QUE NOUS ACCEPTONS</span><small>VIEW ALL</small></div>
    <div class="carousel">
      <div class="arrow"><svg width="7" height="7" viewBox="0 0 10 10"><path d="M7 1L3 5l4 4" stroke="#fff" stroke-width="2" fill="none"/></svg></div>
      <div class="asset"><div class="asset-photo" role="img" aria-label="Photo d'instruments de musique" style="background:linear-gradient(#7a3a12,#b8621f)"></div><span>INSTRUMENT</span></div>
      <div class="asset"><div class="asset-photo" role="img" aria-label="Photo d'équipement high-tech" style="background:linear-gradient(#0b2b6e,#2b6fd1)"></div><span>HIGH-TECH</span></div>
      <div class="asset"><div class="asset-photo" role="img" aria-label="Photo de bijoux" style="background:linear-gradient(#2a2a2a,#6b6b6b)"></div><span>BIJOUX</span></div>
      <div class="asset"><div class="asset-photo" role="img" aria-label="Photo d'une voiture de luxe" style="background:linear-gradient(#cfd3d6,#8c949a)"></div><span>VEHICULES</span></div>
      <div class="asset"><div class="asset-photo" role="img" aria-label="Photo d'une montre de luxe" style="background:linear-gradient(#e4e4e4,#9a9a9a)"></div><span>HORLOGERIE</span></div>
      <div class="asset"><div class="asset-photo" role="img" aria-label="Photo d'une œuvre d'art" style="background:linear-gradient(#c43a2a,#3a6bb0)"></div><span>ART - TABLEAUX</span></div>
      <div class="arrow"><svg width="7" height="7" viewBox="0 0 10 10"><path d="M3 1l4 4-4 4" stroke="#fff" stroke-width="2" fill="none"/></svg></div>
    </div>
  </section>

  <section class="help">
    <h2>BESOIN D'AIDE? NOUS SOMMES À VOTRE ÉCOUTE</h2>
    <div class="help-cols">
      <div class="help-col">
        <svg width="30" height="30" viewBox="0 0 24 24" fill="#fff"><path d="M6.6 10.8a15 15 0 006.6 6.6l2.2-2.2a1 1 0 011-.25 11.4 11.4 0 003.6.6 1 1 0 011 1V20a1 1 0 01-1 1A17 17 0 013 4a1 1 0 011-1h3.5a1 1 0 011 1c0 1.25.2 2.45.6 3.6a1 1 0 01-.25 1z"/></svg>
        <p>Du lundi au vendredi de 9h à 18h</p>
        <strong>0140-5582-36</strong>
      </div>
      <div class="help-col">
        <svg width="30" height="30" viewBox="0 0 24 24" fill="#fff"><path d="M3 4h13v9H8l-4 3v-3H3z"/><path d="M18 8h3v9h-1v3l-3-3h-7v-2h8z"/></svg>
        <p>Une question sur notre service ? Écrivez-nous</p>
        <strong>QUESTIONS FRÉQUENTES</strong>
      </div>
      <div class="help-col">
        <svg width="30" height="30" viewBox="0 0 24 24" fill="none" stroke="#fff" stroke-width="2"><rect x="3" y="5" width="18" height="14"/><path d="M3 5l9 8 9-8"/></svg>
        <p>Envoyez-nous un e-mail, réponse sous 24h</p>
        <strong>CONTACT@MAISON-PRET.FR</strong>
      </div>
    </div>
  </section>

  <section class="testimonials">
    <h2>DERNIERS TÉMOIGNAGES</h2>
    <p>« Un service rapide et discret. J'ai obtenu mon prêt en moins de deux jours en déposant ma montre, et je l'ai récupérée intacte après le remboursement. L'équipe a été disponible du début à la fin et les conditions étaient claires. Je recommande vivement cette solution à tous. »</p>
    <p class="quote-sign">Marc D., a obtenu un prêt de 8 000 € sur sa montre</p>
    <div class="dots"><i></i><i></i><i></i></div>
  </section>

  <section class="counters">
    <div class="counter">
      <div class="digits"><span>0</span><span>0</span><span>4</span><span>4</span><span>8</span><span>9</span></div>
      <p>Objets estimés par nos experts depuis le lancement de notre service en ligne</p>
    </div>
    <div class="counter">
      <div class="digits"><span>0</span><span>0</span><span>0</span><span>4</span><span>2</span><span>1</span></div>
      <p>Prêts accordés à nos clients sur des biens de luxe au cours de l'année</p>
    </div>
  </section>

  <footer class="footer">
    <div class="footer-intro">
      <div class="badge"></div>
      <p>Notre entreprise propose des prêts rapides garantis par vos objets de valeur. Estimation gratuite, fonds versés sous 48h, stockage sécurisé et assuré, rachat possible à tout moment selon vos besoins.</p>
    </div>
    <div class="footer-cols">
      <div class="footer-about">
        <h4>Vendre ou non se racheter</h4>
        <p>Vous souhaitez obtenir des liquidités sans vous séparer définitivement de vos biens ? Notre prêt sur gage vous permet de conserver la propriété de votre objet. À l'échéance, vous choisissez librement de rembourser et récupérer votre bien, ou de le vendre au meilleur prix avec notre accompagnement.</p>
      </div>
      <ul class="footer-links">
        <li>Accueil</li><li>Concept</li><li>Les biens</li><li>Estimation</li><li>FAQ</li><li>Qui sommes-nous ?</li>
      </ul>
      <div class="footer-contact">
        <h4>Contactez-Nous</h4>
        <p>Enterprise<br>14, Rue Belval<br>75011 Paris<br>Tél. 0140-5582-36</p>
      </div>
    </div>
  </footer>
  <div class="bottombar">
    <span>Copyright © 2015 Enterprise. Tous droits réservés.</span>
    <span class="follow">Follow Us :</span>
    <div class="social"><span></span><span></span><span></span></div>
  </div>

</div>
</body>
</html>
```